TeeWiseHub Stationery and Style Guide, You set the tone! (logo Provided)

TeewiseHub is a new and exciting business that will be focusing on providing quality golf information for all Australian golfers.

We already have a great logo and now we are looking to style our documents.

We would like to see the following:

- Front cover page Design including(logo, branding statement and Document title) Branding statement is Every Green - Every Player
- Sales Document design, this is our main document and we would like you to spend most time on this document. I have attached a sample PDF with the basic layout. but you will need to add some flair to the document and make it look great.
- A Dot point design explaining points in an image (I have attached a sample to show what I mean) Please include this image in the Sales Document
- A footnote for all documents(containing, small logo, branding statement and website address)
- An email signature (containing: logo, Dov Hallberg, dov@teewisehub.com.au, 0471 529 318, www.teewisehub.com.au)

The font used in the logo is borisblackboxx.
At this stage we don't need business cards or envelopes please.

A little background:
The service will be providing:

• A Website that allows all Australian golfers to find golf courses close to them on a simple to use Google map
• Browse golf courses on a map or by search.
• View full information about a golf course including images, facilities, prices and full contact details.
• Mobile version of the website for Handset, Android and other mobile platforms.
• We will use the users GPS location to show them where they are and what golf courses are near them.
• All golf courses will be able to show specials and other deals for all visitors.

Thank you for looking at our project and we look forward to your designs.

Target Market(s)

All Australian Golfers

Industry/Entity Type

Golf Course

Requirements
Must have
• A great Sales Document Design as that is the main stationery document we will be using.
Please use the sample Sales Document for sample content and basic elements needed.
Should not have
• We don't need business cards and envelope design.

```html
<!DOCTYPE html>
<html lang="en">
<head>
<meta charset="utf-8">
<title>TeewiseHub Stationery</title>
<link rel="stylesheet" href="https://fonts.googleapis.com/css2?family=Arimo:wght@400;700&display=swap">
<style>
  :root {
    --stage: #e7e2da;
    --paper: #ffffff;
    --frame: #e4e4e4;
    --ink: #6b6b6b;
    --ink-soft: #8a8a8a;
    --accent: #f39a1d;
    --brand: #3c8c23;
    --label: #4a4540;
    --callout: #e8463c;
    --band: #d4d4d4;
  }
  * { margin: 0; padding: 0; box-sizing: border-box; }
  html, body { width: 1200px; height: 561px; overflow: hidden; }
  body {
    position: relative;
    background: var(--stage);
    font-family: "Arimo", Arial, sans-serif;
    color: var(--ink);
  }
  .page {
    position: absolute;
    top: 20px;
    width: 338px;
    height: 438px;
    background: var(--paper);
    box-shadow: 0 1px 4px rgba(0,0,0,.18);
    overflow: hidden;
  }
  .page--cover { left: 42px; }
  .page--intro { left: 426px; }
  .page--benefits { left: 810px; }
  .page__frame {
    position: absolute; inset: 6px;
    border: 1px solid var(--frame);
  }
  .band { position: absolute; top: 0; left: 0; width: 338px; height: 160px; }
  .band--mirrored { transform: scaleX(-1); }

  .brand { position: absolute; top: 44px; }
  .page--cover .brand { left: 16px; }
  .page--intro .brand, .page--benefits .brand { right: 19px; text-align: right; }
  .brand__name {
    display: flex; align-items: center; gap: 4px;
    font-weight: 700; font-size: 13px; color: var(--brand);
    letter-spacing: -.3px;
  }
  .page--intro .brand__name, .page--benefits .brand__name { justify-content: flex-end; }
  .brand__dot { width: 8px; height: 8px; border-radius: 50%; background: var(--brand); }
  .brand__tagline { font-size: 6.6px; font-weight: 700; color: var(--ink-soft); margin-top: 4px; }

  .content { position: absolute; left: 27px; top: 54px; width: 296px; font-size: 6.4px; line-height: 9px; }
  .page--benefits .content { top: 74px; left: 20px; }
  .content h2 { font-size: 8.5px; color: var(--accent); font-weight: 700; margin-bottom: 8px; }
  .content p { margin-bottom: 9px; }
  .content ul { list-style: none; margin-bottom: 9px; }
  .content li { padding-left: 7px; position: relative; }
  .content li::before { content: "•"; position: absolute; left: 0; }

  .footer {
    position: absolute; left: 20px; right: 20px; bottom: 8px;
    display: flex; justify-content: space-between;
    font-size: 5.5px; font-weight: 700; color: var(--accent);
  }

  .feature { position: absolute; left: 0; top: 270px; width: 338px; height: 168px; }
  .feature__screen {
    position: absolute; left: 111px; top: 12px; width: 95px; height: 170px;
    border-radius: 12px;
    background: linear-gradient(160deg, #3a3a3a, #111);
    padding: 18px 6px 0;
  }
  .feature__map {
    width: 100%; height: 120px;
    background: linear-gradient(150deg, #8fb7d8, #cfe0c8 60%, #a9c6e0);
  }
  .callout {
    position: absolute; font-size: 3.6px; line-height: 4.6px;
    font-weight: 700; color: #333; width: 40px; text-transform: uppercase;
  }
  .callout--gps { left: 67px; top: 48px; text-align: right; }
  .callout--special { left: 219px; top: 45px; }
  .callout--drag { left: 55px; top: 113px; text-align: right; }
  .feature__lines { position: absolute; inset: 0; width: 338px; height: 168px; }

  .signature {
    position: absolute; left: 605px; top: 474px; width: 160px; height: 60px;
    background: var(--paper); box-shadow: 0 1px 3px rgba(0,0,0,.18); overflow: hidden;
  }
  .signature .brand { top: 16px; left: 5px; }
  .signature .brand__name { font-size: 10px; gap: 3px; }
  .signature .brand__dot { width: 6px; height: 6px; }
  .signature .brand__tagline { font-size: 4.4px; margin-top: 3px; }
  .signature__band { position: absolute; right: 0; top: 0; width: 80px; height: 40px; }
  .signature__name { position: absolute; right: 8px; top: 9px; font-size: 5px; font-weight: 700; color: var(--ink); }
  .signature__contact { position: absolute; left: 73px; top: 31px; font-size: 4.6px; line-height: 6px; color: var(--ink); }

  .caption { position: absolute; font-size: 10px; color: var(--label); }
  .caption--cover { left: 43px; top: 463px; }
  .caption--intro { left: 426px; top: 463px; }
  .caption--benefits { left: 810px; top: 463px; }
  .caption--signature { left: 648px; top: 537px; }
</style>
</head>
<body>

<section class="page page--cover">
  <div class="page__frame"></div>
  <svg class="band band--mirrored" viewBox="0 0 338 160" aria-hidden="true">
    <polygon points="152,0 186,0 338,98 338,132" fill="var(--band)"/>
  </svg>
  <div class="brand">
    <div class="brand__name"><span class="brand__dot"></span>TeewiseHub</div>
    <div class="brand__tagline">Every Green - Every Player</div>
  </div>
  <div class="footer"><span>Every Green - Every Player</span><span>www.teewisehub.com.au</span></div>
</section>

<section class="page page--intro">
  <div class="page__frame"></div>
  <svg class="band" viewBox="0 0 338 160" aria-hidden="true">
    <polygon points="152,0 186,0 338,98 338,132" fill="var(--band)"/>
  </svg>
  <div class="brand">
    <div class="brand__name"><span class="brand__dot"></span>TeewiseHub</div>
    <div class="brand__tagline">Every Green - Every Player</div>
  </div>
  <div class="content">
    <h2>Introduction</h2>
    <p>Lorem ipsum dolor sit amet, consectetur adipiscing elit.<br>Mauris auctor elit nec neque dictum ultricies. Suspendisse<br>potenti. Etiam eget orci lorem, a commodo enim.</p>
    <p>Donec massa turpis, pulvinar sit amet luctus at, tempor at lorem.<br>Mauris nec massa augue. Phasellus dictum, metus vel posuere ullamcorper,<br>risus erat vehicula magna, id facilisis orci tellus ac magna. Nam a augue lacus,<br>id tempor lorem.</p>
    <p>Mauris odio nunc, dignissim et fermentum eget, venenatis quis turpis. Phasellus<br>faucibus, ligula id pulvinar adipiscing, tortor erat pretium felis, posuere pretium neque<br>nulla pretium lectus.<br>Nulla facilisi. Donec at suscipit quam. Nulla non tortor orci. Fusce purus sem, rutrum<br>et egestas ac, consequat a mi. Curabitur tincidunt massa eget mauris sagittis ornare<br>imperdiet tortor vulputate.</p>
    <p>Aenean blandit eros et neque rhoncus sed tristique ante euismod. Curabitur quis nisi<br>quis mi dapibus faucibus sit amet id enim.</p>
    <p>Ut sed dictum dui. Aenean convallis sagittis ipsum, sed tempor dui ultricies sit amet.<br>Praesent sed erat odio. Duis odio elit, commodo vel luctus non, laoreet at eros.<br>Nullam a mauris metus.</p>
  </div>
  <div class="feature">
    <div class="feature__screen">
      <div class="feature__map" role="img" aria-label="Mobile site screen showing a map of nearby golf courses with location pins"></div>
    </div>
    <svg class="feature__lines" viewBox="0 0 338 168" aria-hidden="true">
      <g stroke="var(--callout)" stroke-width=".8" fill="var(--callout)">
        <line x1="108" y1="54" x2="135" y2="82"/><circle cx="135" cy="82" r="1.6"/>
        <line x1="218" y1="52" x2="180" y2="110"/><circle cx="180" cy="110" r="1.6"/>
        <line x1="98" y1="119" x2="150" y2="119"/><circle cx="98" cy="119" r="1.6"/><circle cx="150" cy="119" r="1.6"/>
      </g>
    </svg>
    <div class="callout callout--gps">Your GPS position shown on map</div>
    <div class="callout callout--special">Post a special to earn a featured listing</div>
    <div class="callout callout--drag">Drag the interactive map to find more courses nearby</div>
  </div>
  <div class="footer"><span>Every Green - Every Player</span><span>www.teewisehub.com.au</span></div>
</section>

<section class="page page--benefits">
  <div class="page__frame"></div>
  <svg class="band" viewBox="0 0 338 160" aria-hidden="true">
    <polygon points="152,0 186,0 338,98 338,132" fill="var(--band)"/>
  </svg>
  <div class="brand">
    <div class="brand__name"><span class="brand__dot"></span>TeewiseHub</div>
    <div class="brand__tagline">Every Green - Every Player</div>
  </div>
  <div class="content">
    <h2>Benefits</h2>
    <p>Lorem ipsum dolor sit amet, consectetur adipiscing elit.<br>Mauris auctor elit nec neque dictum ultricies. Suspendisse potenti.<br>Etiam eget orci lorem, a commodo enim.</p>
    <ul>
      <li>Donec massa turpis, pulvinar sit amet luctus at, tempor at lorem.</li>
      <li>Mauris nec massa augue. Phasellus dictum, metus vel posuere ullamcorper,<br>risus erat vehicula magna, id facilisis orci tellus ac magna.</li>
      <li>Nam a augue lacus, id tempor lorem. Mauris odio nunc, dignissim</li>
      <li>et fermentum eget, venenatis quis turpis. Phasellus faucibus,</li>
      <li>ligula id pulvinar adipiscing, tortor erat pretium felis, posuere</li>
      <li>pretium neque nulla pretium lectus.</li>
      <li>Nulla facilisi. Donec at suscipit quam. Nulla non tortor orci.</li>
      <li>Fusce purus sem, rutrum et egestas ac, consequat a mi.</li>
      <li>Curabitur tincidunt massa eget mauris sagittis</li>
      <li>ornare imperdiet tortor vulputate.</li>
    </ul>
    <p>Aenean blandit eros et neque rhoncus sed tristique ante euismod. Curabitur quis nisi<br>quis mi dapibus faucibus sit amet id enim</p>
    <p>Ut sed dictum dui. Aenean convallis sagittis ipsum, sed tempor dui ultricies sit amet.<br>Praesent sed erat odio. Duis odio elit, commodo vel luctus non, laoreet at eros.<br>Nullam a mauris metus. &nbsp;&nbsp; Aenean blandit eros et neque rhoncus sed tristique ante euis-<br>mod. Curabitur quis nisi<br>quis mi dapibus faucibus sit amet id enim</p>
    <p>Ut sed dictum dui. Aenean convallis sagittis ipsum, sed tempor dui<br>ultricies sit amet.<br>Praesent sed erat odio. Duis odio elit, commodo vel luctus non,<br>laoreet at eros. Nullam a mauris metus.a</p>
  </div>
  <div class="footer"><span>Every Green - Every Player</span><span>www.teewisehub.com.au</span></div>
</section>

<section class="signature">
  <svg class="signature__band" viewBox="0 0 80 40" aria-hidden="true">
    <polygon points="12,0 24,0 80,22 80,31" fill="var(--band)"/>
  </svg>
  <div class="signature__name">Dov Hallberg</div>
  <div class="brand">
    <div class="brand__name"><span class="brand__dot"></span>TeewiseHub</div>
    <div class="brand__tagline">Every Green - Every Player</div>
  </div>
  <div class="signature__contact">
    0471 529 318<br>dov@teewisehub.com.au<br>www.teewisehub.com.au
  </div>
</section>

<div class="caption caption--cover">Document Page 1</div>
<div class="caption caption--intro">Document Page 2</div>
<div class="caption caption--benefits">Document Page 3</div>
<div class="caption caption--signature">Email Signature</div>

</body>
</html>
```